Zelmor Africa - Website Design Brief

Web Design Brief

ZELMOR AFRICA
WEBSITE DESIGN BRIEF

INTRODUCTION
ABOUT ZELMOR
• ZELMOR is a premier consulting firm that specialises in aiding global corporations and emerging businesses to enter and scale within Africa's dynamic markets. Through swift, actionable insights and innovative strategies, ZELMOR empowers clients to capitalise on Africa's untapped potential, thereby catering specifically to forward-thinking entities poised for exponential growth.

TASK DESCRIPTION
• Develop a 5-page website for ZELMOR.
• The primary goal is to present a clear and concise picture of our consulting firm, its Africa-centric experience, and its offerings to multinational clients looking for a professional partner to penetrate African markets or reclaim lost market share.

WEBSITE FRAMEWORK
Page Architecture:
• Home
o A powerful landing page that instantly communicates who ZELMOR is and what solutions it provides. Incorporate impactful visuals and calls-to-action.
• About
o A compelling narrative that illustrates ZELMOR's unique approach to consulting, dedication to Africa, and experience assisting multinational firms.
• Services
o A showcase of ZELMOR's successful projects and client testimonials. This page should build trust and credibility, demonstrating ZELMOR's ability to deliver exceptional results.
• Team
o Introduce up to 8 key team members, with each profile featuring a professional photo, name, title, and a brief bio showcasing the individual's skills, experiences, and contributions to ZELMOR's mission.
• Contact
o Clear and easy ways for visitors to contact ZELMOR for more information or to initiate a partnership.
• Footer
o Links to ZELMOR's social media profiles on Instagram and LinkedIn, along with a privacy policy.
o Social links
o Instagram: https://www.instagram.com/zelmorafrica/
o LinkedIn: https://www.linkedin.com/company/zelmorafrica/
o Privacy Policy
o Insert placeholder "lorem ipsum" text.
o Text will be provided with the revision round or ZELMOR will update text on site handover.

DESIGN INSPIRATION
• The website's design should evoke professionalism and elegance, with simple and clean lines inspired by site pages like:
o https://quendaro.example/
o https://quendaro.example/services/
o One aspect we particularly appreciate is how visitors can easily navigate by scrolling down to find what they're looking for and see everything they need to in an intuitive way on the home page
o What we don’t like about this site is how they navigate from the home page to other random pages – we like about to take you to the about page, and so on.

Branding Guidelines:
• See logo on Pixel Bazaar: Design #: 58170926
• We like the idea of the logo being black or white and have uploaded these options as well.
• Monochrome themes, with spots or splash of colour to highlight something is a style we appreciate.

Website Objectives and Goals:
• Our website's primary goal is to create a strong online presence, acting as a hub for potential clients to discover our credibility, reliability, and our ability to deliver exceptional results. It's essential that our website portrays professionalism, instils trustworthiness, and showcases our sincere dedication to Africa.

Target audience:
• ZELMOR's audience consists of businesses in mobile money, gaming, FMCG, beverage, and alcohol sectors, primarily Business Development Managers or Operations Managers who are seeking insight into their respective marketplaces.

Company Overview:
• ZELMOR stands out from the crowd as a consulting firm with a difference. Our dynamic team is fully dedicated to one mission: brand development within Africa.
• Unlike other companies that focus solely on online connectivity, we recognize the tremendous value in embracing the vibrant street culture that makes Africa so unique. Community engagement, empowerment, and expansion are at the forefront of everything we do.
• we recognize that unlocking business growth starts with a deep understanding of consumer behavior. It is this understanding that bridges the gap between companies and the communities that drive the cash economy. Our purpose is to reconnect businesses with the vibrant pulse of these essential local markets, injecting fresh vitality into their brands and propelling them towards resounding success in Africa.

Development to include:
• Basic SEO Setup:
o The website should be optimized for search engines, incorporating keywords, meta tags, and alt tags for images.
• Google Analytics Setup.
o To track website traffic and user behaviour for ongoing optimization.
• Google Crawling Setup
o The website needs to be easily indexed by Google, allowing it to appear in search results, and updated information effectively crawled by Google SEO and AHREFS scores.

PAGE CONTENT:
Home Page
• Background
o Option #1
o 4K video on home page, running on loop
o Bold Statement Text over Video
o Option #2
o Still Image
o Animated text making bold statement (e.g. our motto)

• Sections
o Contrast colour blocks or a way of making it clear that the next topic is a new topic.
o 5 sections
1. Home Main - Video + bold statement text
2. About - A paragraph and visual about us (lorem ipsum) that has a click through to our About Page (ignore how quendaro.example navigate, we think this is too complicated for our needs)
3. Services – communicated in some simple and powerful ways (we leave this open to you) – but keeping in mind it needs to be concise and professional.
4. Other - Something about our process that makes us unique (lorem ipsum text) and a placeholder image/animation.
5. Contact – a call-to-action button that takes you to our contact, but showcases a mobile number and email address.
6. Footer – as described in the previous section – placeholder for Instagram and LinkedIn only.

About Page
• Don’t reference quendaro.example for this page.
• Main Section
o Bold statements and images
• History Section
o A story about us and our past
• Final Section
o Some of our comments and final thoughts

Services Page
• How https://quendaro.example/services/ is laid out is great – we prefer a light theme.
• 6 - 8 x icons with headings and a brief description text box, and a read more drop down – all as placeholders to be edited later.
• For ease of direction for this page, look to the link shared above.

Team
• Add Placeholders for up to 8 team members (we only have 4 now):
o Image placeholder
o Name placeholder
o Title placeholder
o Short Bio (lorem ipsum)

Contact
• Clear and easy ways for visitors to contact ZELMOR for more information or to initiate a partnership.

• Insert placeholder "lorem ipsum" text, we will provide the text with our revision round.
o Ideally an easy form process that gives the user some options or dropdowns to complete before submission – up to 3 would be sufficient.
o Require their name and contact details.

NOTE: Images to follow:

Target Market(s)

ZELMOR's audience consists of businesses in mobile money, gaming, FMCG, beverage, and alcohol sectors, primarily Business Development Managers or Operations Managers who are seeking insight into their respective marketplaces.

Industry/Entity Type

ZELMOR is a premier consulting firm that specialises in aiding global corporations and emerging businesses to enter and scale within Africa's dynamic markets

Coding

Coded - Design and coding required

Number of Pages Required

5+ page

Font styles to use
Sans Serif
Other font styles liked:
• Poppins Font Family

Colors

Designer to choose colors to be used in the design.

Requirements
Must have
• The primary goal is to present a clear and concise picture of our consulting firm, and it's specialisation in Africa - smooth and crisp UI with animations or transitions that imply we know our way around tecchnology is always helpful - but a Clean and responsive UI is most important.
Nice to have
• Reactive and animated transitions through sections or pages - not overdone - adds a professional feel to the site
Should not have
• We don't want too many colours, and we don't want it too dark - we want a monochrome theme, with accents of colour when relevant

```html
<!DOCTYPE html>
<html lang="en">
<head>
<meta charset="utf-8">
<title>Contact Us – ZELMOR</title>
<link rel="stylesheet" href="https://fonts.googleapis.com/css2?family=Poppins:wght@500;600;700&family=Roboto:wght@400;500;700&display=swap">
<style>
:root{
  --ink:#0b0b0b;
  --white:#ffffff;
  --page:#fafafa;
  --body-text:#666666;
  --field-text:#7a7a7a;
  --icon-dark:#3a3a3a;
  --icon-light:#b3b3b3;
  --heading:#3d3d3d;
  --footer-text:#e6e6e6;
  --footer-muted:#c4c4c4;
  --button-light:#dcdcdc;
}
*{margin:0;padding:0;box-sizing:border-box}
html,body{width:954px;height:1200px;overflow:hidden}
body{position:relative;background:var(--page);font-family:'Roboto',sans-serif;color:var(--body-text)}
.abs{position:absolute}

/* hero */
.hero{left:0;top:0;width:954px;height:250px;overflow:hidden}
.hero-photo{position:absolute;inset:0;
  background:linear-gradient(180deg,#474747 0%,#4f4a45 22%,#6b5a4a 48%,#4d5a46 70%,#3f3a34 100%)}
.hero-shade{position:absolute;inset:0;background:rgba(0,0,0,.18)}
.brand{left:100px;top:8px;font-family:'Poppins',sans-serif;font-weight:700;font-size:34px;color:var(--white);letter-spacing:.5px}
.nav{right:103px;top:25px;display:flex;gap:15px;list-style:none}
.nav a{font-family:'Poppins',sans-serif;font-weight:500;font-size:13px;color:var(--white);text-decoration:none}
.hero-title{left:0;width:954px;top:117px;text-align:center;font-family:'Poppins',sans-serif;font-weight:700;font-size:31px;color:var(--white);letter-spacing:-.5px}

/* contact form */
.intro{left:197px;width:560px;top:301px;text-align:center;font-size:10px;line-height:15px}
.field{background:var(--white);border:1px solid #e4e4e4;border-radius:3px;box-shadow:0 2px 5px rgba(0,0,0,.14);
  font-family:'Roboto',sans-serif;font-size:9px;color:var(--field-text);padding:13px 14px;outline:none;resize:none}
.field::placeholder{color:var(--field-text)}
.submit{left:420px;top:558px;width:120px;height:34px;border:none;border-radius:17px;background:var(--ink);color:var(--white);
  font-family:'Roboto',sans-serif;font-weight:700;font-size:11px;letter-spacing:.3px}

/* info cards */
.info{width:200px;text-align:center}
.info-icon{width:55px;height:55px;border-radius:50%;margin:0 auto;display:flex;align-items:center;justify-content:center}
.info-icon.dark{background:var(--icon-dark)}
.info-icon.light{background:var(--icon-light)}
.info-title{font-family:'Poppins',sans-serif;font-weight:600;font-size:19px;color:var(--heading);margin-top:4px;line-height:26px}
.info-rule{width:28px;height:2px;background:var(--heading);margin:3px auto 0}
.info-text{font-size:10px;color:#444;margin-top:9px}

/* footer */
.footer{left:0;top:830px;width:954px;height:370px;
  background:linear-gradient(180deg,#171717 0%,#141414 45%,#1e1e1e 80%,#262626 100%);border-top:1px solid #2a2a2a}
.footer-divider{left:415px;top:830px;width:4px;height:370px;background:#0c0c0c}
.footer-heading{font-family:'Roboto',sans-serif;font-weight:500;font-size:13.5px;color:var(--footer-text)}
.quick-links{left:103px;top:934px;list-style:none}
.quick-links li{height:26.2px}
.quick-links a{font-size:10px;font-weight:500;color:var(--footer-text);text-decoration:none}
.ci-label{font-size:12px;font-weight:500;color:var(--footer-text);display:flex;align-items:center;gap:4px}
.ci-value{font-size:9.5px;color:var(--footer-muted);margin:4px 0 0 15px}
.social{width:33px;height:33px;border:1px solid #e0e0e0;border-radius:50%;display:block}
.ft-field{left:521px;width:331px;background:transparent;border:1px solid #cfcfcf;font-family:'Roboto',sans-serif;font-size:9px;color:var(--footer-text);padding:0 11px;outline:none;resize:none}
.ft-field::placeholder{color:#dcdcdc}
.ft-submit{left:521px;top:1096px;width:121px;height:35px;border:none;background:var(--button-light);font-family:'Roboto',sans-serif;font-weight:700;font-size:13px;color:#222}
.copyright{left:104px;top:1167px;font-size:10px;color:#bdbdbd}
</style>
</head>
<body>

<header class="abs hero">
  <div class="hero-photo" role="img" aria-label="Aerial photo of a busy African city with rooftops, a market road and a pedestrian bridge"></div>
  <div class="hero-shade"></div>
</header>
<div class="abs brand">ZELMOR</div>
<ul class="abs nav">
  <li><a href="#">HOME</a></li>
  <li><a href="#">ABOUT</a></li>
  <li><a href="#">SERVICES</a></li>
  <li><a href="#">TEAM</a></li>
  <li><a href="#">CONTACT</a></li>
</ul>
<h1 class="abs hero-title">CONTACT US</h1>

<p class="abs intro">Lorem ipsum dolor sit amet, consectetur adipiscing elit. Phasellus ac velit porttitor, euismod dolor sit amet, cursus nisl. Aenean interdum rutrum elit quis sodales. Integer mollis venenatis leo pellentesque ultrices.</p>

<input class="abs field" style="left:177px;top:357px;width:294px;height:38px" placeholder="Name">
<input class="abs field" style="left:482px;top:357px;width:294px;height:38px" placeholder="Email">
<input class="abs field" style="left:177px;top:408px;width:600px;height:38px" placeholder="Phone">
<textarea class="abs field" style="left:177px;top:456px;width:600px;height:73px" placeholder="Message"></textarea>
<button class="abs submit">SUBMIT</button>

<div class="abs info" style="left:166px;top:663px">
  <div class="info-icon dark">
    <svg width="20" height="28" viewBox="0 0 20 28"><path d="M10 0C4.5 0 0 4.4 0 9.8 0 16.5 10 28 10 28s10-11.5 10-18.2C20 4.4 15.5 0 10 0z" fill="#fff"/><circle cx="10" cy="9.8" r="3.8" fill="#3a3a3a"/></svg>
  </div>
  <div class="info-title">Address</div>
  <div class="info-rule"></div>
  <div class="info-text" style="margin-left:20px">4120 Harbour Rd NE Kelby</div>
</div>

<div class="abs info" style="left:388px;top:663px">
  <div class="info-icon light">
    <svg width="24" height="24" viewBox="0 0 24 24"><path d="M6.6 2.5l2.6 4.2c.4.6.2 1.3-.3 1.7l-1.6 1.2c1 2.3 2.7 4.2 5 5.5l1.3-1.5c.4-.5 1.2-.6 1.7-.2l4.1 2.7c.6.4.7 1.2.3 1.7l-1.6 2c-.8 1-2.2 1.3-3.4.8C8.5 18.4 4.6 14.3 2.6 8.1c-.4-1.2 0-2.5 1-3.3l2-1.6c.4-.4 1-.3 1 .3z" fill="#fff"/><path d="M14 3.5a7 7 0 016.5 6.5M14 6.5a4 4 0 013.5 3.5" stroke="#fff" stroke-width="1.4" fill="none" stroke-linecap="round"/></svg>
  </div>
  <div class="info-title">Phone</div>
  <div class="info-rule"></div>
  <div class="info-text" style="margin-left:8px">+ (305) 555-0192</div>
</div>

<div class="abs info" style="left:604px;top:663px">
  <div class="info-icon dark">
    <svg width="28" height="20" viewBox="0 0 28 20"><rect x="1" y="1" width="26" height="18" fill="none" stroke="#fff" stroke-width="1.5"/><path d="M1 1l13 10L27 1M1 19l10-9M27 19l-10-9" fill="none" stroke="#fff" stroke-width="1.5"/></svg>
  </div>
  <div class="info-title">Email</div>
  <div class="info-rule"></div>
  <div class="info-text">info@Zelmor.com</div>
</div>

<footer class="abs footer" role="img" aria-label="Dark monochrome photo of a crowded city street with a crane in the background"></footer>
<div class="abs footer-divider"></div>

<h3 class="abs footer-heading" style="left:103px;top:900px">QUICK LINKS</h3>
<ul class="abs quick-links">
  <li><a href="#">HOME</a></li>
  <li><a href="#">ABOUT US</a></li>
  <li><a href="#">SERVICES</a></li>
  <li><a href="#">TEAM</a></li>
  <li><a href="#">CONTACT</a></li>
  <li><a href="#">PRIVACY POLICY</a></li>
</ul>

<h3 class="abs footer-heading" style="left:283px;top:900px">CONTACT INFO</h3>
<div class="abs" style="left:282px;top:934px">
  <div class="ci-label"><svg width="11" height="11" viewBox="0 0 24 24"><path d="M6.6 2.5l2.6 4.2c.4.6.2 1.3-.3 1.7l-1.6 1.2c1 2.3 2.7 4.2 5 5.5l1.3-1.5c.4-.5 1.2-.6 1.7-.2l4.1 2.7c.6.4.7 1.2.3 1.7l-1.6 2c-.8 1-2.2 1.3-3.4.8C8.5 18.4 4.6 14.3 2.6 8.1c-.4-1.2 0-2.5 1-3.3l2-1.6c.4-.4 1-.3 1 .3z" fill="#e6e6e6"/></svg>PHONE</div>
  <div class="ci-value">(03) 7024 5519</div>
</div>
<div class="abs" style="left:282px;top:981px">
  <div class="ci-label"><svg width="11" height="9" viewBox="0 0 28 20"><rect x="1.5" y="1.5" width="25" height="17" fill="none" stroke="#e6e6e6" stroke-width="2.5"/><path d="M1.5 1.5l12.5 10 12.5-10" fill="none" stroke="#e6e6e6" stroke-width="2.5"/></svg>EMAIL</div>
  <div class="ci-value">info@ZELMOR.com</div>
</div>
<a class="abs social" style="left:282px;top:1033px" href="#" aria-label="Social profile"></a>
<a class="abs social" style="left:324px;top:1033px" href="#" aria-label="Social profile"></a>

<h3 class="abs footer-heading" style="left:520px;top:899px">GET IN TOUCH</h3>
<input class="abs ft-field" style="top:937px;height:31px" placeholder="Enter your name">
<input class="abs ft-field" style="top:977px;height:32px" placeholder="Enter your email">
<textarea class="abs ft-field" style="top:1018px;height:70px;padding-top:9px" placeholder="Enter your massage"></textarea>
<button class="abs ft-submit">SUBMIT NOW</button>

<p class="abs copyright">© 2023 ZELMOR.com. All rights reserved.</p>

</body>
</html>
```